Postcard promoting HIPAA services, including training, risk assessments, policies, etc.

I am planning a campaign to medical practices advertising HIPAA services. The primary message to convey is that HIPAA random audits are beginning in early 2016, is your practice ready. I need a full-color front design, 4.25 x 6. The design should convey some sense of urgency, and should be dramatic enough to catch the attention of a busy medical practice.

Target Market(s)

Medical, dental, chiropractic, and counseling practices

Industry/Entity Type

Doctor

Font styles to use
Sans Serif

Requirements
Must have
• Sense of urgency, specific mention of upcoming HIPAA audits, feeling that smaller practices are not exempt.

```html
<!DOCTYPE html>
<html lang="en">
<head>
<meta charset="utf-8">
<title>HIPAA Random Audits – Postcard Front</title>
<link rel="stylesheet" href="https://fonts.googleapis.com/css2?family=Anton&family=Oswald:wght@600&family=Archivo+Narrow:wght@400;700&family=Pinyon+Script&display=swap">
<style>
  :root {
    --ink: #0d0d0d;
    --alert-red: #d8252e;
    --corridor-light: #eefcfd;
    --corridor-mid: #9fdde3;
    --corridor-deep: #3c9fab;
    --corridor-shadow: #1f6f7b;
  }

  html, body {
    margin: 0;
    padding: 0;
    width: 1200px;
    height: 850px;
    overflow: hidden;
    background: #ffffff;
  }

  .postcard {
    position: relative;
    width: 1200px;
    height: 850px;
    overflow: hidden;
  }

  .corridor-backdrop {
    position: absolute;
    inset: 0;
    background:
      radial-gradient(ellipse 42% 38% at 52% 30%, var(--corridor-light) 0%, rgba(238,252,253,0.6) 45%, rgba(238,252,253,0) 100%),
      radial-gradient(ellipse 70% 60% at 50% 55%, var(--corridor-mid) 0%, rgba(159,221,227,0.4) 60%, rgba(159,221,227,0) 100%),
      linear-gradient(90deg, var(--corridor-deep) 0%, var(--corridor-mid) 22%, var(--corridor-light) 50%, var(--corridor-mid) 78%, var(--corridor-deep) 100%),
      linear-gradient(180deg, var(--corridor-mid) 0%, var(--corridor-light) 45%, var(--corridor-deep) 100%);
    background-blend-mode: normal, normal, multiply, normal;
  }

  .corridor-backdrop::after {
    content: "";
    position: absolute;
    inset: 0;
    background: linear-gradient(180deg, rgba(31,111,123,0) 70%, rgba(31,111,123,0.25) 100%);
  }

  .headline {
    position: absolute;
    left: 352px;
    top: 300px;
    margin: 0;
    color: var(--ink);
  }

  .headline-acronym {
    display: block;
    font-family: "Anton", "Oswald", sans-serif;
    font-weight: 400;
    font-size: 156px;
    line-height: 1;
    letter-spacing: -1px;
    transform: scaleX(1.05);
    transform-origin: left center;
  }

  .headline-audits {
    display: block;
    margin-top: 4px;
    font-family: "Oswald", sans-serif;
    font-weight: 600;
    font-size: 72px;
    line-height: 0.9;
    letter-spacing: -2px;
    color: var(--alert-red);
    text-transform: uppercase;
  }

  .headline-date {
    display: block;
    margin-top: 6px;
    font-family: "Archivo Narrow", sans-serif;
    font-size: 50px;
    line-height: 1.1;
    font-weight: 400;
    color: var(--ink);
  }

  .headline-date strong {
    font-weight: 700;
  }

  .readiness-question {
    position: absolute;
    left: 244px;
    top: 596px;
    margin: 0;
    font-family: "Pinyon Script", cursive;
    font-size: 72px;
    line-height: 1;
    color: var(--ink);
    white-space: nowrap;
  }
</style>
</head>
<body>
  <main class="postcard">
    <div class="corridor-backdrop" role="img" aria-label="Photograph of a bright, empty hospital corridor in pale teal light"></div>

    <h1 class="headline">
      <span class="headline-acronym">HIPAA</span>
      <span class="headline-audits">Random Audits</span>
      <span class="headline-date">beginning <strong>EARLY 2016</strong></span>
    </h1>

    <p class="readiness-question">Is your practice ready?</p>
  </main>
</body>
</html>
```